"MEET THE TEAM" page web design

We need a "meet the team" page for our website!
Please look at our website to see the style we need

We are looking for something unique, fun, cool, technology-style and yet professional. We plan on taking a picture of each employee (not sure if this will be a real photo/caricature/ black and white/goofy picture--> but we are open to any ideas you have that will work with the design) and putting it there, along with a little bio about each person.

Thanks! looking forward to working together:)
Updates

Project Deadline Extended
Reason: I am excited to see more designs and find the perfect fit. Thanks designers :)

Target Market(s)

People looking to purchase servers, workstations, components

Industry/Entity Type

Information Technology

Number of Pages Required

1 page

Font styles to use
Sans Serif
Other font styles liked:
• The font we use on our site so it matches

Requirements
Must have
• please look at our website qondimex.com and see the theme and colors we want.
• We have 13 employees but would like to have a design where we can add/remove people if we hire/terminate them without messing up the design.
• We are looking for something unique, fun, cool, technology-style and yet professional. We plan on taking a picture of each employee (not sure if this will be a real photo/caricature/ black and white/goofy picture--> but we are open to any ideas you have that will work with the design) and putting it there, along with a little bio about each person.
• We can upload anything you need
Nice to have
• We are also interested in having a design where when the cursor moves over a person then the bio comes out or moves around, or something. (This is not required, but we would love some cool ideas) And if you can come up with some design, we would have our programmers create it for us.
Should not have
• we are open to anything

```html
<!DOCTYPE html>
<html lang="en">
<head>
<meta charset="utf-8">
<title>Meet the Team – Qondimex</title>
<link href="https://fonts.googleapis.com/css2?family=Open+Sans:wght@400;600;700&display=swap" rel="stylesheet">
<style>
:root{
  --teal:#12a990;
  --teal-soft:#8fd3c5;
  --teal-line:#3bbfa8;
  --ink:#222;
  --rule:#d6d6d6;
  --footer:#a5a5a5;
  --footer-deep:#9b9b9b;
  --white:#fff;
}
*{box-sizing:border-box;margin:0;padding:0}
html,body{width:1200px;height:2510px;overflow:hidden}
body{position:relative;background:var(--white);font-family:"Open Sans",Arial,sans-serif;color:var(--ink)}

/* header */
.brand{position:absolute;left:64px;top:25px;display:flex;align-items:center;gap:16px}
.brand-mark{width:60px;height:60px;border-radius:50%;background:var(--teal)}
.brand-name{font-size:42px;font-weight:600;color:var(--teal);line-height:1}
.account-tab{position:absolute;left:947px;top:0;width:191px;height:33px;border-radius:0 0 22px 22px;background:linear-gradient(#c9c9c9,#a9a9a9);display:flex;font-size:11px;color:#444}
.account-tab span{flex:1;display:flex;align-items:center;justify-content:center}
.account-tab span+span{border-left:1px solid #999}
.contact-quick{position:absolute;top:46px;display:flex;align-items:center;gap:10px;font-size:15px;color:#555}
.contact-quick .ring{width:40px;height:40px;border-radius:50%;border:1px solid #cfcfcf;display:flex;align-items:center;justify-content:center}
.contact-quick.chat{left:835px}
.contact-quick.phone{left:972px;font-size:20px;color:#333}

.main-nav{position:absolute;left:0;top:102px;width:1200px;height:50px;border-top:1px solid #ddd;border-bottom:3px solid var(--teal-line);display:flex;align-items:center}
.main-nav ul{list-style:none;display:flex;margin-left:62px}
.main-nav li{font-size:11px;color:#333;text-transform:uppercase;margin-right:29px}
.search{position:absolute;left:930px;top:8px;width:165px;height:34px;border:1px solid #bbb;border-radius:17px;font-size:11px;color:#444;padding:9px 16px;display:flex;justify-content:space-between;align-items:center}
.cart{position:absolute;left:1105px;top:6px;width:38px;height:38px;border-radius:50%;border:1px solid #bbb;display:flex;align-items:center;justify-content:center}

.page-banner{position:absolute;left:0;top:152px;width:1200px;height:94px;background:linear-gradient(90deg,#e3e3e3 0%,#d2d2d2 40%,#c6c6c6 60%,#e0e0e0 100%)}
.page-title{position:absolute;left:65px;top:33px;font-size:20px;font-weight:700;color:#222}
.breadcrumb{position:absolute;right:57px;top:36px;font-size:15px;font-weight:600;color:var(--teal)}
.breadcrumb b{color:#222}

/* team */
.member{position:absolute;left:60px;width:1083px;height:276px;display:flex}
.member .photo{width:287px;height:276px;flex:none}
.member .info{margin-left:60px;width:736px}
.member .name{font-size:16.5px;font-weight:700;text-transform:uppercase;padding:4px 0 9px;border-bottom:1px solid var(--rule)}
.member .bio{font-size:18.5px;line-height:30px;margin-top:14px}
.member .phone{font-size:16px;line-height:22px;margin-top:28px}
.member .email{font-size:13.5px;line-height:20px;color:var(--teal);margin-top:7px}
.member .socials{display:flex;gap:6px;margin-top:28px}
.member .socials i{width:29px;height:29px;border-radius:50%;background:var(--teal-soft);display:block}
.member.separated::after{content:"";position:absolute;left:0;right:0;bottom:-26px;border-bottom:1px solid var(--rule)}

.member.featured{top:308px;height:326px;background:var(--teal);color:var(--white);border-left:2px solid var(--teal)}
.member.featured .photo{height:326px}
.member.featured .info{margin-left:58px}
.member.featured .name{padding-top:21px;padding-bottom:15px;border-color:rgba(255,255,255,.25)}
.member.featured .bio{margin-top:13px}
.member.featured .phone{color:#bff0e5;margin-top:15px}
.member.featured .email{color:#dff7f1;margin-top:1px}
.member.featured .socials{margin-top:18px}
.member.featured .socials i{background:#7fd6c5}

/* footer */
.site-footer{position:absolute;left:0;top:2020px;width:1200px;height:311px;background:var(--footer);color:var(--white)}
.footer-about{position:absolute;left:368px;top:17px;width:520px;text-align:center;font-size:15px;line-height:20px;border-bottom:1px solid #c4c4c4;padding-bottom:2px}
.footer-contacts{position:absolute;left:364px;top:146px;display:flex;gap:34px;font-size:15px;line-height:20px}
.footer-contacts div{display:flex;gap:10px;align-items:flex-start}
.footer-links{position:absolute;left:331px;top:208px;display:flex;font-size:15px}
.footer-links .c1{width:136px}
.footer-links .c2{width:97px}
.footer-links .c3{width:112px}
.footer-links .c4{width:89px}
.footer-links ul{list-style:none;font-size:9.5px;text-align:center;line-height:14px;margin-top:6px}
.footer-base{position:absolute;left:0;top:2331px;width:1200px;height:179px;background:var(--footer-deep);color:var(--white)}
.footer-social{position:absolute;left:491px;top:22px;display:flex;gap:15px}
.footer-social i{width:38px;height:38px;border-radius:50%;border:1px solid #d6d6d6;display:block}
.footer-rule{position:absolute;left:190px;width:820px;top:81px;border-top:1px solid #b9b9b9}
.copyright{position:absolute;left:548px;top:96px;display:flex;gap:12px;align-items:center;font-size:13px;line-height:18px}
.copyright i{width:22px;height:22px;background:#e5e5e5;display:block}
.chat-now{position:absolute;left:972px;top:2484px;width:213px;height:26px;background:var(--teal-line);color:var(--white);font-size:13px;font-weight:700;padding:4px 10px;display:flex;justify-content:space-between;border:1px solid #e9e9e9}
</style>
</head>
<body>

<header>
  <div class="brand">
    <span class="brand-mark"></span>
    <span class="brand-name">QONDIMEX</span>
  </div>
  <div class="account-tab"><span>SIGN UP</span><span>LOGIN</span></div>
  <div class="contact-quick chat">
    <span class="ring"><svg width="20" height="16" viewBox="0 0 20 16"><path d="M2 2h12v8H7l-4 3v-3H2z" fill="#12a990"/><path d="M15 5h3v7h-1v2l-3-2H9v-1h6z" fill="#12a990"/></svg></span>
    LIVE CHAT
  </div>
  <div class="contact-quick phone">
    <span class="ring"><svg width="18" height="18" viewBox="0 0 24 24"><path d="M6.6 10.8a15 15 0 0 0 6.6 6.6l2.2-2.2a1 1 0 0 1 1-.25 11.4 11.4 0 0 0 3.6.57 1 1 0 0 1 1 1V20a1 1 0 0 1-1 1A17 17 0 0 1 3 4a1 1 0 0 1 1-1h3.5a1 1 0 0 1 1 1c0 1.25.2 2.45.57 3.57a1 1 0 0 1-.25 1z" fill="#12a990"/></svg></span>
    555-014-2290
  </div>
  <nav class="main-nav">
    <ul>
      <li>Servers</li><li>Workstations</li><li>Components</li><li>Virtual Reality</li><li>Drones</li><li>About Us</li><li>Blog</li><li>Resources</li><li>Contact Us</li>
    </ul>
    <div class="search">Search
      <svg width="14" height="14" viewBox="0 0 14 14"><circle cx="6" cy="6" r="4.5" fill="none" stroke="#12a990" stroke-width="2"/><path d="M9.5 9.5L13 13" stroke="#12a990" stroke-width="2"/></svg>
    </div>
    <div class="cart">
      <svg width="18" height="16" viewBox="0 0 18 16"><path d="M1 5h16l-2 9H3z" fill="none" stroke="#12a990" stroke-width="2"/><path d="M5 5l3-4M13 5l-3-4" stroke="#12a990" stroke-width="1.6"/></svg>
    </div>
  </nav>
  <div class="page-banner" role="img" aria-label="Banner background showing server hardware in soft grey tones">
    <h1 class="page-title">MEET THE TEAM</h1>
    <div class="breadcrumb">HOME <b>/</b> OUR TEAM</div>
  </div>
</header>

<main>
  <article class="member featured">
    <div class="photo" role="img" aria-label="Portrait photo of a team member in a dark blazer" style="background:linear-gradient(160deg,#e6e6e6,#b9b9b9 55%,#2c2c30)"></div>
    <div class="info">
      <h2 class="name">Evan R. Castell</h2>
      <p class="bio">Lorem ipsum dolor sit amet, consectetur adipiscing elit. In vehicula bibendum elit, at vestibulum enim tempor a. Nulla ultrices erat et erat aliquet aliquet. Nunc ligula nulla, cursus non nunc et, elementum ultrices arcu.Nulla ultrices erat et erat aliquet aliq Nulla ultrices erat et erat aliquet aliq</p>
      <p class="phone">Phone: (012) 555 - 0143</p>
      <p class="email">lorem ipsu@rollmark-contact.com</p>
      <div class="socials"><i></i><i></i><i></i><i></i></div>
    </div>
  </article>

  <article class="member separated" style="top:671px">
    <div class="photo" role="img" aria-label="Portrait photo of a team member in a white jacket" style="background:linear-gradient(160deg,#ededed,#d9d4cf 55%,#5b4a40)"></div>
    <div class="info">
      <h2 class="name">Evan R. Castell</h2>
      <p class="bio">Lorem ipsum dolor sit amet, consectetur adipiscing elit. In vehicula bibendum elit, at vestibulum enim tempor a. Nulla ultrices erat et erat aliquet aliquet. Nunc ligula nulla, cursus non nunc et, elementum ultrices arcu.</p>
      <p class="phone">Phone: (012) 555 - 0143</p>
      <p class="email">lorem ipsu@rollmark-contact.com</p>
      <div class="socials"><i></i><i></i><i></i><i></i></div>
    </div>
  </article>

  <article class="member separated" style="top:1006px">
    <div class="photo" role="img" aria-label="Portrait photo of a team member in a checked shirt" style="background:linear-gradient(160deg,#dfe3e6,#c9ced3 50%,#3b4a60)"></div>
    <div class="info">
      <h2 class="name">Evan R. Castell</h2>
      <p class="bio">Lorem ipsum dolor sit amet, consectetur adipiscing elit. In vehicula bibendum elit, at vestibulum enim tempor a. Nulla ultrices erat et erat aliquet aliquet. Nunc ligula nulla, cursus non nunc et, elementum ultrices arcu.</p>
      <p class="phone">Phone: (012) 555 - 0143</p>
      <p class="email">lorem ipsu@rollmark-contact.com</p>
      <div class="socials"><i></i><i></i><i></i><i></i></div>
    </div>
  </article>

  <article class="member separated" style="top:1342px">
    <div class="photo" role="img" aria-label="Portrait photo of a team member in a suit in an office" style="background:linear-gradient(160deg,#c8d3dc,#9aa7b3 50%,#20242c)"></div>
    <div class="info">
      <h2 class="name">Evan R. Castell</h2>
      <p class="bio">Lorem ipsum dolor sit amet, consectetur adipiscing elit. In vehicula bibendum elit, at vestibulum enim tempor a. Nulla ultrices erat et erat aliquet aliquet. Nunc ligula nulla, cursus non nunc et, elementum ultrices arcu.</p>
      <p class="phone">Phone: (012) 555 - 0143</p>
      <p class="email">lorem ipsu@rollmark-contact.com</p>
      <div class="socials"><i></i><i></i><i></i><i></i></div>
    </div>
  </article>

  <article class="member separated" style="top:1680px">
    <div class="photo" role="img" aria-label="Portrait photo of a team member in a suit against a sky" style="background:linear-gradient(160deg,#b7cde6,#9fb8d3 45%,#1d1f24)"></div>
    <div class="info">
      <h2 class="name">Evan R. Castell</h2>
      <p class="bio">Lorem ipsum dolor sit amet, consectetur adipiscing elit. In vehicula bibendum elit, at vestibulum enim tempor a. Nulla ultrices erat et erat aliquet aliquet. Nunc ligula nulla, cursus non nunc et, elementum ultrices arcu.</p>
      <p class="phone">Phone: (012) 555 - 0143</p>
      <p class="email">lorem ipsu@rollmark-contact.com</p>
      <div class="socials"><i></i><i></i><i></i><i></i></div>
    </div>
  </article>
</main>

<footer>
  <div class="site-footer">
    <p class="footer-about">Based in Westbrook California, Qondimex offers custom servers, storage, and workstations for local businesses in Los Angeles, Beverly Hills, Thousand Oaks, Ventura, Orange County, Santa Barbara, Oxnard, Irvine, Anaheim, and San Diego. Qondimex also offers such products to clients throughout the United States and Worldwide.</p>
    <div class="footer-contacts">
      <div><svg width="12" height="16" viewBox="0 0 12 16"><path d="M6 0a6 6 0 0 0-6 6c0 4 6 10 6 10s6-6 6-10a6 6 0 0 0-6-6zm0 8.5A2.5 2.5 0 1 1 6 3.5a2.5 2.5 0 0 1 0 5z" fill="#fff"/></svg><span>4120 Marlow Ave.<br>Westbrook, CA 90210</span></div>
      <div><svg width="14" height="14" viewBox="0 0 24 24"><path d="M6.6 10.8a15 15 0 0 0 6.6 6.6l2.2-2.2a1 1 0 0 1 1-.25 11.4 11.4 0 0 0 3.6.57 1 1 0 0 1 1 1V20a1 1 0 0 1-1 1A17 17 0 0 1 3 4a1 1 0 0 1 1-1h3.5a1 1 0 0 1 1 1c0 1.25.2 2.45.57 3.57a1 1 0 0 1-.25 1z" fill="#fff"/></svg><span>555-014-2290</span></div>
      <div><svg width="16" height="12" viewBox="0 0 16 12"><rect width="16" height="12" fill="#fff"/><path d="M0 0l8 6 8-6" fill="none" stroke="#a5a5a5" stroke-width="1.5"/></svg><span>sales@qondimex.com</span></div>
    </div>
    <div class="footer-links">
      <div class="c1">Computers</div>
      <div class="c2">Drones</div>
      <div class="c3">Virtual</div>
      <div class="c4">About</div>
      <div class="support">Customer Support
        <ul><li>Terms and<br>Conditions</li><li>Warranty Information</li><li>Contact Us</li><li>Return Policy</li></ul>
      </div>
    </div>
  </div>
  <div class="footer-base">
    <div class="footer-social"><i></i><i></i><i></i><i></i></div>
    <div class="footer-rule"></div>
    <div class="copyright"><i></i><span>Qondimex, LLC.<br>Copyright © 2017</span></div>
  </div>
  <div class="chat-now">CHAT NOW
    <svg width="14" height="14" viewBox="0 0 14 14"><path d="M2 10l5-5 5 5" fill="none" stroke="#fff" stroke-width="2"/></svg>
  </div>
</footer>

</body>
</html>
```